I have a business that exists already (Wrenfield Academy of Music) that we offer music lessons to all instruments. I recently opened a smaller version called CHORDS by Wrenfield that will only teach piano lessons. What I'm looking for now is a 3 page Website on word press. After I choose the design I like I want to be able to take over the website and bring it to our hosting company. We want full control of it and our team will take over. The reason I'm doing this is to have other visions and ideas from others. The first page will be about the company and our message/vision. Second page about the piano lessons. The third will be about franchising this concept "Chords by Wrenfield" Attached are 3 Logos . Please refer to our existing website www.wrenfieldmusicacademy.example to look at our piano page and franchising page. Please feel free to message me if you need more info. Thanks
Please note I do not want the new website (Chords by Wrenfield) To look like the other Website (Wrenfield Academy of Music) Fresh new look. I do not want the colours red or using the Red logo. I only provided it so that you have an Idea of What the other business looks like and that you can take the piano content and franchise content off of it. Chords by Wrenfield is smaller concept and only piano lessons.
Thanks
Target Market(s)
Only Piano lessons for all students
Number of Pages Required
3 page
Look and feel

```html
<!DOCTYPE html>
<html lang="en">
<head>
<meta charset="utf-8">
<title>CHORDS by Wrenfield – Piano Lessons</title>
<link rel="stylesheet" href="https://fonts.googleapis.com/css2?family=Playfair+Display:wght@700&family=Crimson+Text:wght@400;600&family=Lato:wght@400;700&family=Libre+Baskerville:wght@400;700&display=swap">
<style>
:root{
  --orange:#f05a2a;
  --orange-soft:#f26a3c;
  --black:#000;
  --white:#fff;
  --yellow:#f3e20c;
  --ink:#1b1b1b;
  --body:#444;
  --field-line:#d9d9d9;
  --field-text:#777;
}
*{box-sizing:border-box;margin:0;padding:0}
html,body{width:1200px;height:3820px;overflow:hidden}
body{position:relative;background:var(--white);font-family:"Lato",sans-serif;color:var(--body)}
.abs{position:absolute}
.btn{position:absolute;display:flex;align-items:center;justify-content:center;background:var(--orange);color:var(--white);font-family:"Libre Baskerville",serif;font-weight:700;font-size:17px;text-transform:uppercase;letter-spacing:.3px;text-decoration:none}
.btn--white{background:var(--white);color:var(--orange)}

/* header */
.site-header{position:absolute;left:0;top:0;width:1200px;height:159px;background:var(--black)}
.brand{position:absolute;color:var(--white);font-family:"Crimson Text",serif;font-weight:400;line-height:1}
.brand--header{left:52px;top:46px;font-size:46px}
.brand small{display:block;font-size:26px;margin-top:4px;padding-left:70px}
.social{position:absolute;display:flex;gap:11px}
.social span{display:block;width:36px;height:36px;border-radius:50%;background:var(--white)}
.social--header{left:974px;top:30px}
.main-nav a{position:absolute;top:102px;color:var(--white);font-size:19px;text-decoration:none}

/* hero (children positioned relative to the hero) */
.hero{position:absolute;left:0;top:159px;width:1200px;height:640px}
.hero-photo{position:absolute;inset:0;background:linear-gradient(100deg,#1a1410 0%,#3b2a1e 35%,#6a5240 60%,#2a1f17 100%)}
.hero-kicker{position:absolute;left:52px;top:135px;font-family:"Crimson Text",serif;font-size:60px;color:var(--white);line-height:1}
.hero-title{position:absolute;left:52px;top:190px;font-size:76px;color:var(--white);line-height:1}
.hero-text{position:absolute;left:52px;top:275px;font-family:"Crimson Text",serif;font-size:21px;line-height:28px;color:var(--white)}
.hero-tag{position:absolute;left:52px;top:345px;font-family:"Libre Baskerville",serif;font-weight:700;font-size:35px;line-height:1;color:var(--yellow)}

/* about */
.about-title{position:absolute;left:52px;top:905px;font-family:"Playfair Display",serif;font-weight:700;font-size:53px;line-height:1;color:var(--ink)}
.about-title em{font-style:normal;color:var(--orange)}
.about-text{position:absolute;left:52px;width:520px;font-size:18px;line-height:26px;color:var(--body)}
.about-art{position:absolute;left:575px;top:823px;width:605px;height:475px;background:radial-gradient(ellipse at 55% 55%,#5a3a28 0%,#2a2320 45%,rgba(255,255,255,0) 72%)}

/* vision */
.vision{position:absolute;left:0;top:1400px;width:1200px;height:531px;background:linear-gradient(90deg,#e9582c,#f26a3c 50%,#f07a4c)}
.vision h2{position:absolute;left:0;width:1200px;top:118px;text-align:center;font-family:"Playfair Display",serif;font-size:59px;line-height:1.1;color:var(--white)}
.vision p{position:absolute;left:226px;width:748px;top:191px;text-align:center;font-size:18px;line-height:28px;color:var(--white)}

/* instructors */
.instructors{position:absolute;left:0;top:1931px;width:1200px;height:540px;background:linear-gradient(90deg,#0b0a09,#1f1b17 55%,#3a332c)}
.instructors h2{position:absolute;left:50px;top:88px;font-family:"Crimson Text",serif;font-weight:400;font-size:58px;line-height:61px;color:var(--white)}
.instructors p{position:absolute;left:50px;top:290px;font-size:21px;line-height:33px;color:var(--white)}

/* contact */
.contact-eyebrow{position:absolute;left:0;width:1200px;top:2568px;text-align:center;font-family:"Libre Baskerville",serif;font-size:29px;color:#f57a1f}
.contact-title{position:absolute;left:0;width:1200px;top:2604px;text-align:center;font-family:"Playfair Display",serif;font-size:62px;line-height:1.2;color:var(--ink)}
.field{position:absolute;border:1px solid var(--field-line);padding:0 17px;font-size:16px;color:var(--field-text);display:flex;align-items:center}
.field--area{align-items:flex-start;padding-top:22px}

/* footer */
.footer-band{position:absolute;left:0;top:3140px;width:1200px}
.site-footer{position:absolute;left:0;top:3240px;width:1200px;height:535px;background:var(--black)}
.brand--footer{left:37px;top:3318px;font-size:46px}
.footer-about{position:absolute;left:52px;top:3461px;width:320px;font-size:15.5px;line-height:26px;color:#bbb}
.social--footer{left:52px;top:3635px;gap:10px}
.social--footer span{width:44px;height:44px;background:var(--orange)}
.footer-head{position:absolute;font-family:"Crimson Text",serif;font-size:25px;color:var(--white);text-transform:uppercase}
.footer-list{position:absolute;list-style:none;font-size:14.5px;color:#bbb;text-transform:uppercase}
.contact-line{position:absolute;left:446px;color:var(--white)}
.contact-line b{display:block;font-family:"Crimson Text",serif;font-weight:400;font-size:24px;padding-left:21px;line-height:30px}
.contact-line span{display:block;font-size:21px;color:#bbb;padding-left:21px}
.contact-line svg{position:absolute;left:0;top:6px}
.insta-tile{position:absolute;width:82px;height:82px}
.copyright{position:absolute;left:0;top:3775px;width:1200px;height:45px;background:var(--orange);color:var(--white);font-family:"Crimson Text",serif;font-size:15px;display:flex;align-items:center;justify-content:center}
</style>
</head>
<body>

<header class="site-header">
  <div class="brand brand--header">CHORDS<small>by Wrenfield</small></div>
  <a class="btn" style="left:776px;top:19px;width:158px;height:57px">Contact Us</a>
  <div class="social social--header"><span></span><span></span><span></span><span></span></div>
  <nav class="main-nav">
    <a style="left:688px">ABOUT</a>
    <a style="left:788px">LESSONS &amp; PROGRAMS</a>
    <a style="left:1022px">FRANCHISING</a>
  </nav>
</header>

<section class="hero">
  <div class="hero-photo" role="img" aria-label="Close-up of hands playing a grand piano keyboard"></div>
  <div class="hero-kicker">Piano lessons for</div>
  <div class="hero-title">All Students</div>
  <p class="hero-text">Fusce eu lectus sit amet nibh accumsan eleifend.<br>Vivamus quis nisl augue. Vestibulum dignissim,</p>
  <div class="hero-tag">A CHORDS by Wrenfield</div>
  <a class="btn" style="left:52px;top:408px;width:178px;height:56px">Contact Us</a>
</section>
<svg class="abs" style="left:0;top:690px" width="1200" height="110" viewBox="0 0 1200 110" aria-hidden="true">
  <path d="M0 28 C220 -10 400 110 660 104 C880 98 1000 20 1200 14 L1200 110 L0 110Z" fill="#fff"/>
  <path d="M0 28 C220 -10 400 110 660 104 C880 98 1000 20 1200 14" fill="none" stroke="var(--orange)" stroke-width="6"/>
</svg>

<section class="about">
  <h2 class="about-title"><em>About</em> The Company</h2>
  <p class="about-text" style="top:969px">Mauris sed orci cursus, egestas urna ut, finibus metus. Suspendisse porttitor augue vel mi convallis, non maximus est imperdiet. Pellentesque rhoncus dictum sem, sed mollis sapien facilisis sed. Sed nec congue nisi, eu mollis ligula. Aliquam ut nisi non ex efficitur sodales eleifend vel est. Proin venenatis in risus ac condimentum. Integer orci metus</p>
  <p class="about-text" style="top:1140px;width:490px">Duis eget lacinia est, in tempor libero. Aliquam nec eleifend arcu. Integer ultricies rutrum ex, vel viverra neque facilisis viverra.</p>
  <a class="btn" style="left:52px;top:1241px;width:178px;height:58px">Contact Us</a>
  <div class="about-art" role="img" aria-label="Splashed ink illustration of piano keys with a pianist's hands"></div>
</section>

<section class="vision">
  <div class="abs" style="inset:0;background:linear-gradient(90deg,rgba(120,40,20,.25),rgba(0,0,0,0) 40%,rgba(255,255,255,.08))" role="img" aria-label="Young woman playing an upright piano, tinted orange"></div>
  <h2>Our vision</h2>
  <p>When you think of a piano, you probably envision black and white keys but the piano is more than those harmonious sounds created by the player. The versatility and the musicianship instilled into the player from those keys is the true magic that comes from playing piano! Starting from the grassroots, experience different methods and styles of playing piano.</p>
  <a class="btn btn--white" style="left:511px;top:350px;width:178px;height:56px">Contact Us</a>
</section>

<section class="instructors">
  <div class="abs" style="inset:0" role="img" aria-label="Student in a knit sweater playing piano in a dim room"></div>
  <h2>Our instructors Are<br>Passionate and<br>Experienced</h2>
  <p>Fusce ante mi, interdum sit amet purus ut, faucibus pretium velit.<br>Maecenas interdum neque a tempor fringilla.</p>
  <a class="btn" style="left:52px;top:388px;width:168px;height:57px">Sign Up!</a>
</section>

<section class="contact">
  <div class="contact-eyebrow">REACH OUT TO WRENFIELD</div>
  <h2 class="contact-title">Comments? Questions?</h2>
  <div class="field" style="left:52px;top:2695px;width:259px;height:50px">Name:</div>
  <div class="field" style="left:331px;top:2695px;width:259px;height:50px">Email:</div>
  <div class="field" style="left:609px;top:2695px;width:260px;height:50px">Phone No:</div>
  <div class="field" style="left:887px;top:2695px;width:261px;height:50px">Student Age:</div>
  <div class="field" style="left:52px;top:2759px;width:538px;height:50px">Location:</div>
  <div class="field" style="left:609px;top:2759px;width:539px;height:50px">Program:</div>
  <div class="field field--area" style="left:52px;top:2824px;width:1096px;height:142px">Comments:</div>
  <a class="btn" style="left:511px;top:2990px;width:178px;height:56px">Contact Us</a>
</section>

<svg class="footer-band" height="110" viewBox="0 0 1200 110" aria-hidden="true">
  <path d="M0 92 C180 30 380 4 600 12 C820 20 1020 60 1200 100 L1200 110 L0 110Z" fill="#000"/>
  <path d="M0 92 C180 30 380 4 600 12 C820 20 1020 60 1200 100" fill="none" stroke="var(--orange)" stroke-width="6"/>
</svg>
<footer class="site-footer"></footer>
<div class="brand brand--footer">CHORDS<small>by Wrenfield</small></div>
<p class="footer-about">Mauris sed orci cursus, egestas urna ut, finibus metus. Suspendisse porttitor augue vel mi convallis, non maximus est imperdiet. Pellentesque rhoncus dictum sem, sed mollis sapien facilisis sed. Sed nec congue nisi, eu mollis ligula. Ali-</p>
<div class="social social--footer"><span></span><span></span><span></span><span></span></div>

<div class="footer-head" style="left:446px;top:3326px">Quick Link</div>
<ul class="footer-list" style="left:449px;top:3388px;line-height:32px">
  <li>About</li><li>Lesson</li><li>Franchising</li>
</ul>
<div class="contact-line" style="top:3545px">
  <svg width="12" height="22" viewBox="0 0 12 22"><path d="M9 1 C3 4 3 18 9 21" fill="none" stroke="var(--orange)" stroke-width="4" stroke-linecap="round"/></svg>
  <b>INQUIRIES:</b><span>1-888-555-0142</span>
</div>
<div class="contact-line" style="top:3622px">
  <svg width="12" height="22" viewBox="0 0 12 22"><path d="M9 1 C3 4 3 18 9 21" fill="none" stroke="var(--orange)" stroke-width="4" stroke-linecap="round"/></svg>
  <b>FRANCHISING:</b><span>905-555-0187</span>
</div>

<div class="footer-head" style="left:682px;top:3328px">Lessons</div>
<ul class="footer-list" style="left:688px;top:3389px;line-height:32.6px">
  <li>Fusce ante mi,</li><li>Interdum sit amet</li><li>Purus ut,</li><li>Faucibus</li><li>Pretium velit.</li><li>Maecenas</li><li>Interdum</li><li>Nequea</li><li>Tempor fringilla.</li>
</ul>

<div class="footer-head" style="left:887px;top:3324px">Instagram</div>
<div class="insta-tile" style="left:887px;top:3393px;background:linear-gradient(135deg,#e8e4de,#9a948c)" role="img" aria-label="Instagram photo: student at the piano"></div>
<div class="insta-tile" style="left:979px;top:3393px;background:linear-gradient(135deg,#d9cbbb,#6a5546)" role="img" aria-label="Instagram photo: piano lesson"></div>
<div class="insta-tile" style="left:1068px;top:3393px;background:linear-gradient(135deg,#3a3430,#c9b6a2)" role="img" aria-label="Instagram photo: hands on keys"></div>
<div class="insta-tile" style="left:887px;top:3482px;background:linear-gradient(135deg,#e8e4de,#9a948c)" role="img" aria-label="Instagram photo: student at the piano"></div>
<div class="insta-tile" style="left:979px;top:3482px;background:linear-gradient(135deg,#d9cbbb,#6a5546)" role="img" aria-label="Instagram photo: piano lesson"></div>
<div class="insta-tile" style="left:1068px;top:3482px;background:linear-gradient(135deg,#3a3430,#c9b6a2)" role="img" aria-label="Instagram photo: hands on keys"></div>
<div class="insta-tile" style="left:887px;top:3574px;background:linear-gradient(135deg,#e8e4de,#9a948c)" role="img" aria-label="Instagram photo: student at the piano"></div>
<div class="insta-tile" style="left:979px;top:3574px;background:linear-gradient(135deg,#d9cbbb,#6a5546)" role="img" aria-label="Instagram photo: piano lesson"></div>
<div class="insta-tile" style="left:1068px;top:3574px;background:linear-gradient(135deg,#3a3430,#c9b6a2)" role="img" aria-label="Instagram photo: hands on keys"></div>

<div class="copyright">© 2020 - CHORDS by Wrenfield. All Right Reserved.</div>

</body>
</html>
```